Renaldo's Motorworks landing page to Dealership page, Rental Car Page, and Auto Body page.

I'm looking for my website to have RenaldosMotor.com be the landing page. From there visitors will have the option to visit three pages. My auto dealer page, of which I will provide an example of how I'd like it done. Auto body page, where I will fill in the text. The rental car page. Basically on the auto dealer and rental page I'll need the ability to add vehicles and delete as I need. Otherwise, its a pretty straightforward site. Nothing extensive. I already have the logo design from a previous project on here completed and can provide. If more funded needed for page capabilities, I can provide. I do have an account with NetHarbor, with renaldosmotor.com already under them.

Target Market(s)

Automotive

Industry/Entity Type

Auto body repair, dealership, rental car.

Coding

Coded - Design and coding required

Number of Pages Required

4 page

Font styles to use
Sans Serif

Colors
0054AA
0677BA
7BADD7
CADEEF
E8F1F8

Requirements
Must have
• My logo Renaldos Motorworks at the top. Be creative with pics in the background of cars.
Nice to have
• Ease of use with being able to add vehicles for sale, and rental cars.
Should not have
• Nothing complex, would like to get in and out. Nothing to extensive on the designs of the pages, simple but attractive.

```html
<!DOCTYPE html>
<html lang="en">
<head>
<meta charset="utf-8">
<title>Renaldo's Motorworks</title>
<link href="https://fonts.googleapis.com/css2?family=Rubik:wght@400;500;700;800&family=Oswald:wght@600&display=swap" rel="stylesheet">
<style>
:root{
  --blue:#0677BA;
  --blue-deep:#0054AA;
  --blue-bright:#1b78cc;
  --blue-soft:#7BADD7;
  --blue-pale:#CADEEF;
  --blue-mist:#E8F1F8;
  --ink:#111418;
  --text:#2b2f36;
  --muted:#7a7f88;
  --line:#e6e9ee;
  --footer:#121212;
  --white:#ffffff;
}
*{box-sizing:border-box;margin:0;padding:0}
html,body{width:1200px;height:2606px;overflow:hidden}
body{position:relative;background:var(--white);font-family:'Rubik',sans-serif;color:var(--text)}
.abs{position:absolute}

/* header */
.site-header{position:absolute;top:0;left:0;width:1200px;height:101px;background:var(--white)}
.brand{position:absolute;left:162px;top:32px;display:flex;align-items:center;gap:8px}
.brand-dot{width:14px;height:14px;border-radius:50%;background:var(--blue)}
.brand-name{font-size:17px;font-weight:700;color:var(--blue-deep);line-height:1.1;width:110px}
.main-nav{position:absolute;left:412px;top:52px;display:flex;gap:0;font-size:12.5px;letter-spacing:.2px;color:#333}
.main-nav a{color:inherit;text-decoration:none;margin-right:19px}
.phone-line{position:absolute;left:845px;top:58px;width:218px;height:1px;background:var(--blue)}
.phone-btn{position:absolute;left:862px;top:35px;width:181px;height:46px;background:var(--blue);color:var(--white);display:flex;align-items:center;justify-content:center;gap:10px;font-weight:500;font-size:14px}

/* hero */
.hero{position:absolute;top:101px;left:0;width:1200px;height:386px;
  background:radial-gradient(ellipse 180px 140px at 52% 5%,rgba(240,120,60,.75),transparent),
  radial-gradient(ellipse 260px 200px at 62% 40%,rgba(220,230,240,.35),transparent),
  linear-gradient(90deg,#25282e 0%,#3b414b 30%,#5a6676 48%,#2c4a78 66%,#1d3d6e 85%,#2a4f86 100%)}
.hero-title{position:absolute;left:158px;top:107px;font-size:32px;font-weight:800;color:var(--white);line-height:39px;letter-spacing:.3px}
.hero-sub{position:absolute;left:158px;top:199px;font-size:13px;color:var(--white);line-height:24px;width:310px}

/* services */
.photo{position:absolute}
.photo-left{left:0;top:552px;width:360px;height:480px;background:linear-gradient(135deg,#d8dde2,#b1343c 55%,#7d1a22)}
.photo-right{left:871px;top:697px;width:295px;height:320px;background:linear-gradient(160deg,#e9ecef,#c8ccd2 40%,#1f2f5a 70%,#8e1b25)}
.services-title{position:absolute;left:399px;top:569px;font-size:24px;font-weight:700;color:var(--ink);letter-spacing:.2px}
.service{position:absolute;left:386px;width:460px}
.service-icon{position:absolute;left:0;top:0;width:72px;height:64px}
.service-name{position:absolute;left:84px;top:0;font-size:16px;color:var(--ink)}
.service-text{position:absolute;left:84px;top:25px;width:370px;font-size:12.5px;line-height:24px;color:var(--muted)}

/* brands */
.brands{position:absolute;top:1085px;left:0;width:1200px;height:479px;
  background:radial-gradient(ellipse 420px 200px at 75% 80%,rgba(70,85,110,.45),transparent),linear-gradient(180deg,#1a2130,#131a28 60%,#0f1522)}
.brands-title{position:absolute;top:55px;left:0;width:1200px;text-align:center;font-family:'Oswald',sans-serif;font-weight:600;font-size:26px;color:var(--white);letter-spacing:.3px}
.brand-tile{position:absolute;width:160px;height:92px;background:var(--white);display:flex;align-items:center;justify-content:center;font-size:18px;font-weight:700;color:#1d2b4a}
.dot{position:absolute;width:7px;height:7px;border-radius:50%;background:var(--blue-bright)}
.dot-active{width:22px;height:22px;background:rgba(27,120,204,.25);display:flex;align-items:center;justify-content:center}
.dot-active span{width:7px;height:7px;border-radius:50%;background:var(--blue-bright)}

/* offers */
.offer-banner{position:absolute;left:155px;top:1626px;width:282px;height:340px;
  background:radial-gradient(ellipse 160px 90px at 60% 30%,rgba(30,150,200,.35),transparent),linear-gradient(170deg,#0c1c2a,#06101a 60%,#020407)}
.offer-kicker{position:absolute;left:26px;top:186px;font-size:18px;font-weight:700;color:var(--blue-bright)}
.offer-big{position:absolute;left:26px;top:210px;font-size:46px;font-weight:800;color:var(--blue-bright)}
.offer-note{position:absolute;left:32px;top:276px;font-size:13px;line-height:24px;color:var(--white);width:220px}
.part-card{position:absolute;width:281px;height:103px;border:1px solid var(--line);background:var(--white)}
.part-photo{position:absolute;left:14px;top:20px;width:66px;height:60px;border-radius:6px;background:radial-gradient(circle,#9aa0a8,#e4e6ea 70%)}
.part-name{position:absolute;left:95px;top:22px;font-size:15px;color:var(--ink)}
.part-text{position:absolute;left:95px;top:45px;width:175px;font-size:11px;line-height:17px;color:var(--muted)}
.part-arrow{position:absolute;right:0;bottom:0;width:26px;height:22px;background:var(--blue);color:var(--white);font-size:12px;display:flex;align-items:center;justify-content:center}

/* testimonials */
.eyebrow{position:absolute;left:156px;top:2035px;font-size:11px;color:var(--blue);letter-spacing:.2px}
.testi-title{position:absolute;left:156px;top:2060px;font-size:24px;font-weight:700;color:var(--ink)}
.testi-lead{position:absolute;left:157px;top:2105px;font-size:13px;color:var(--muted)}
.nav-circle{position:absolute;top:2139px;width:42px;height:42px;border-radius:50%;background:#f4f5f7;color:#b8bcc3;display:flex;align-items:center;justify-content:center;font-size:18px}
.quote-card{position:absolute;top:2025px;width:303px;height:163px;border:1px solid #eef0f3;border-radius:14px;background:var(--white);box-shadow:0 4px 16px rgba(20,40,80,.05)}
.quote-text{position:absolute;left:34px;top:16px;width:250px;font-size:13px;line-height:24px;color:var(--muted)}
.avatar{position:absolute;left:34px;top:102px;width:42px;height:42px;border-radius:50%;background:#eceef1}
.client-name{position:absolute;left:90px;top:106px;font-size:13px;font-weight:500;color:var(--ink)}
.client-role{position:absolute;left:90px;top:124px;font-size:12px;color:#b7bbc2}
.quote-mark{position:absolute;left:234px;top:112px}

/* footer */
.site-footer{position:absolute;left:0;top:2239px;width:1200px;height:367px;background:var(--footer);color:var(--white)}
.footer-brand{position:absolute;left:158px;top:78px;display:flex;align-items:center;gap:8px}
.footer-brand .brand-name{color:var(--white)}
.footer-about{position:absolute;left:156px;top:157px;width:205px;font-size:11px;line-height:18px}
.footer-heading{position:absolute;top:63px;font-size:16px;font-weight:700}
.contact-item{position:absolute;left:412px;display:flex;align-items:center;gap:12px;font-size:13px}
.quick-link{position:absolute;left:663px;font-size:13px}
.social{position:absolute;top:100px;width:23px;height:23px;border:1.5px solid var(--white);border-radius:50%}
.copyright{position:absolute;top:316px;left:0;width:1200px;text-align:center;font-size:11px}
</style>
</head>
<body>

<header class="site-header">
  <div class="brand"><span class="brand-dot"></span><span class="brand-name">Renaldo's Motorworks</span></div>
  <nav class="main-nav">
    <a href="#">HOME</a><a href="#">DEALERSHIP</a><a href="#">CAR RENTAL</a><a href="#">AUTO BODY</a><a href="#">CONTACT US</a>
  </nav>
  <div class="phone-line"></div>
  <div class="phone-btn">
    <svg width="18" height="18" viewBox="0 0 24 24" fill="none" stroke="#fff" stroke-width="1.6"><path d="M5 3h4l2 5-2.5 1.5a11 11 0 0 0 6 6L16 13l5 2v4a2 2 0 0 1-2 2A16 16 0 0 1 3 5a2 2 0 0 1 2-2z"/></svg>
    (555) 310-2874
  </div>
</header>

<section class="hero" role="img" aria-label="Mechanic aligning the wheel of a blue car in a workshop">
  <h1 class="hero-title">YOUR CAR IS IN THE<br>RIGHT HANDS.</h1>
  <p class="hero-sub">Luxury Cars at low-cost, starts $75 / day from over 100 premium locations</p>
</section>

<section class="services">
  <div class="photo photo-left" role="img" aria-label="Smiling man leaning on the door of a red car"></div>
  <h2 class="services-title">WHY YOUR SHOULD USE OUR SERVICES</h2>

  <div class="service" style="top:652px">
    <svg class="service-icon" viewBox="0 0 72 64" fill="none" stroke="#0677BA" stroke-width="1.6"><rect x="8" y="14" width="26" height="40"/><path d="M8 24h26M21 14v40M14 8c3-4 7 0 7 6 0-6 4-10 7-6"/><circle cx="44" cy="34" r="13"/><path d="M47 29c-2-2-7-1-6 2s7 2 6 5-5 3-7 1M44 26v18"/></svg>
    <h3 class="service-name">Cheapest Price on the Market</h3>
    <p class="service-text">Lorem ipsum dolor sit amet, consectetur adipiscing elit. Duis consequat mi neque, id varius quam mollis quis. Duis facilisis justo lectus, vitae tempor diam tincidunt et.</p>
  </div>
  <div class="service" style="top:787px">
    <svg class="service-icon" viewBox="0 0 72 64" fill="none" stroke="#0677BA" stroke-width="1.6"><path d="M6 52V42l6-12h30l8 12h10v10z"/><circle cx="18" cy="52" r="5"/><circle cx="50" cy="52" r="5"/><rect x="36" y="6" width="24" height="14"/><path d="M48 9v8M10 24c2-8 10-14 22-14"/></svg>
    <h3 class="service-name">Easiest Way to Sell Your Car</h3>
    <p class="service-text">Lorem ipsum dolor sit amet, consectetur adipiscing elit. Duis consequat mi neque, id varius quam mollis quis. Duis facilisis justo lectus, vitae tempor diam tincidunt et.</p>
  </div>
  <div class="service" style="top:919px">
    <svg class="service-icon" viewBox="0 0 72 64" fill="none" stroke="#0677BA" stroke-width="1.6"><circle cx="30" cy="30" r="12"/><path d="M14 30a16 16 0 0 1 32 0M14 30v8h4v-8zM46 30v8h-4M12 58c2-8 9-12 18-12s16 4 18 12"/><rect x="46" y="6" width="18" height="12"/><path d="M50 18l-2 5 6-5"/></svg>
    <h3 class="service-name">24 Hour Call Service</h3>
    <p class="service-text">Lorem ipsum dolor sit amet, consectetur adipiscing elit. Duis consequat mi neque, id varius quam mollis quis. Duis facilisis justo lectus, vitae tempor diam tincidunt et.</p>
  </div>

  <div class="photo photo-right" role="img" aria-label="Man crouching to inspect the wheel of a red car"></div>
</section>

<section class="brands" role="img" aria-label="Dark car interior dashboard backdrop">
  <h2 class="brands-title">CHOOSE CARS BY BRAND</h2>
  <div class="brand-tile" style="left:155px;top:139px">Norvik</div>
  <div class="brand-tile" style="left:337px;top:139px">Castellan</div>
  <div class="brand-tile" style="left:520px;top:139px">Hawthorne</div>
  <div class="brand-tile" style="left:702px;top:139px">Velmar</div>
  <div class="brand-tile" style="left:883px;top:139px">Arcline</div>
  <div class="brand-tile" style="left:155px;top:259px">Kestrel</div>
  <div class="brand-tile" style="left:337px;top:259px">Duvall</div>
  <div class="brand-tile" style="left:520px;top:259px">Brightwing</div>
  <div class="brand-tile" style="left:702px;top:259px">Solano</div>
  <div class="brand-tile" style="left:883px;top:259px">Meridian</div>
  <span class="dot" style="left:567px;top:405px"></span>
  <span class="dot dot-active" style="left:591px;top:398px"><span></span></span>
  <span class="dot" style="left:637px;top:405px"></span>
</section>

<section class="offers">
  <div class="offer-banner" role="img" aria-label="Luxury car cockpit with glowing blue dashboard">
    <p class="offer-kicker">Take care of</p>
    <p class="offer-big">22% off</p>
    <p class="offer-note">This discount is not valid in conjunction with other offers</p>
  </div>

  <article class="part-card" style="left:461px;top:1627px">
    <div class="part-photo" role="img" aria-label="Car engine block"></div>
    <h3 class="part-name">OE Replacement Engine</h3>
    <p class="part-text">While they were the darling of the "yuppie" class.</p>
    <span class="part-arrow">›</span>
  </article>
  <article class="part-card" style="left:763px;top:1627px">
    <div class="part-photo" role="img" aria-label="Red racing seat"></div>
    <h3 class="part-name">OE Replacement Engine</h3>
    <p class="part-text">While they were the darling of the "yuppie" class.</p>
  </article>
  <article class="part-card" style="left:461px;top:1741px">
    <div class="part-photo" role="img" aria-label="Turbocharger"></div>
    <h3 class="part-name">OE Replacement Engine</h3>
    <p class="part-text">While they were the darling of the "yuppie" class.</p>
  </article>
  <article class="part-card" style="left:763px;top:1741px">
    <div class="part-photo" role="img" aria-label="Car headlight unit"></div>
    <h3 class="part-name">OE Replacement Engine</h3>
    <p class="part-text">While they were the darling of the "yuppie" class.</p>
  </article>
  <article class="part-card" style="left:461px;top:1863px">
    <div class="part-photo" role="img" aria-label="Red coilover shock absorber"></div>
    <h3 class="part-name">OE Replacement Engine</h3>
    <p class="part-text">While they were the darling of the "yuppie" class.</p>
  </article>
  <article class="part-card" style="left:763px;top:1863px">
    <div class="part-photo" role="img" aria-label="Cone air filter"></div>
    <h3 class="part-name">OE Replacement Engine</h3>
    <p class="part-text">While they were the darling of the "yuppie" class.</p>
  </article>
</section>

<section class="testimonials">
  <p class="eyebrow">TESTIMONIALS</p>
  <h2 class="testi-title">What Clients Say About Us</h2>
  <p class="testi-lead">Lorem ipsum dolor sit amet, consectetur adipiscing elit.</p>
  <span class="nav-circle" style="left:157px">←</span>
  <span class="nav-circle" style="left:219px">→</span>

  <article class="quote-card" style="left:537px">
    <p class="quote-text">Lorem ipsum dolor sit amet, consectetur adipiscing elit. Ut elit tellus, luctus nec ullamcorper mattis, pulvinar</p>
    <div class="avatar" role="img" aria-label="Client portrait"></div>
    <p class="client-name">Nora Quill</p>
    <p class="client-role">client</p>
    <svg class="quote-mark" width="32" height="20" viewBox="0 0 32 20" fill="#1b78cc"><path d="M6 0h8L8 20H0zM22 0h8l-6 20h-8z"/></svg>
  </article>
  <article class="quote-card" style="left:868px">
    <p class="quote-text">Lorem ipsum dolor sit amet, consectetur adipiscing elit. Ut elit tellus, luctus nec ullamcorper mattis, pulvinar</p>
    <div class="avatar" role="img" aria-label="Client portrait"></div>
    <p class="client-name">Dean Hollis</p>
    <p class="client-role">client</p>
    <svg class="quote-mark" width="32" height="20" viewBox="0 0 32 20" fill="#1b78cc"><path d="M6 0h8L8 20H0zM22 0h8l-6 20h-8z"/></svg>
  </article>
</section>

<footer class="site-footer">
  <div class="footer-brand"><span class="brand-dot"></span><span class="brand-name">Renaldo's Motorworks</span></div>
  <p class="footer-about">Lorem ipsum dolor sit amet, consecte­tur adipiscing elit. Quisque pharetra condimentum.</p>

  <h4 class="footer-heading" style="left:412px">Our Address</h4>
  <p class="contact-item" style="top:106px"><svg width="16" height="16" viewBox="0 0 24 24" fill="none" stroke="#fff" stroke-width="1.6"><path d="M12 22s7-7 7-12a7 7 0 0 0-14 0c0 5 7 12 7 12z"/><circle cx="12" cy="10" r="2.5"/></svg>418 Larkspur Ave, Dunmore</p>
  <p class="contact-item" style="top:151px"><svg width="16" height="16" viewBox="0 0 24 24" fill="none" stroke="#fff" stroke-width="1.6"><path d="M5 3h4l2 5-2.5 1.5a11 11 0 0 0 6 6L16 13l5 2v4a2 2 0 0 1-2 2A16 16 0 0 1 3 5a2 2 0 0 1 2-2z"/></svg>+1 555 014 2290</p>
  <p class="contact-item" style="top:196px"><svg width="16" height="16" viewBox="0 0 24 24" fill="none" stroke="#fff" stroke-width="1.6"><rect x="3" y="5" width="18" height="14"/><path d="M3 5l9 8 9-8"/></svg>hello@renaldosmotor.com</p>
  <p class="contact-item" style="top:241px"><svg width="16" height="16" viewBox="0 0 24 24" fill="none" stroke="#fff" stroke-width="1.6"><circle cx="12" cy="12" r="9"/><path d="M12 7v5l3 2"/></svg>09.00 - 17.00</p>

  <h4 class="footer-heading" style="left:659px">Quick Links</h4>
  <a class="quick-link" style="top:106px">Home</a>
  <a class="quick-link" style="top:138px">Dealership</a>
  <a class="quick-link" style="top:170px">Car Rental</a>
  <a class="quick-link" style="top:202px">Auto Body</a>
  <a class="quick-link" style="top:234px">Contact us</a>

  <h4 class="footer-heading" style="left:871px">Follow Us</h4>
  <span class="social" style="left:872px" aria-label="Social profile"></span>
  <span class="social" style="left:905px" aria-label="Social profile"></span>
  <span class="social" style="left:938px" aria-label="Social profile"></span>
  <span class="social" style="left:972px" aria-label="Social profile"></span>

  <p class="copyright">Copyright © 2021 RenaldosMotor.com.</p>
</footer>

</body>
</html>
```